3D Scans and Virtual Tour photography company needs a website

We need a website build that explains what we do, shows some examples of our 3d scans and virtual tours, some stats on why they are important when when selling your home or marketing your business/premises and a contact form to find out more. We need to target both the real estate agents and consumers. The site needs to looks modern, engaging, clean, not lots of text but more pictures and icons. Needs to be mobile friendly. In fact i would build it from the mobile then out.
Updates

Project Deadline Extended
Reason: Hi Team, I have had a couple of requests to extend the Project deadline, which I have now done. I cant push it much more than this as the business is up and running now and I need the website. Looking forward to reviewing the designs.

Target Market(s)

people selling their home and the real estate industry mostly, however any building can be scanned and have a 3d tour

Industry/Entity Type

Photographer

Font styles to use
Sans Serif

Colors
32a6d6
0355a3
33a6d7
85cae6
cee9f5
3176b5

Requirements
Must have
• Our logo
• an example of the 3d scans
• an example of a dollhouse view
• a contact page
• Replace the orange document examples to blue please
• social media links Quillnest Pondlarken Zembol
Nice to have
• some examples of similar companies websites we like
• favourite would be this one hollanbrick (dot com)
• next fav orvantile (dot com au) and brevolux (dot com au)

```html
<!DOCTYPE html>
<html lang="en">
<head>
<meta charset="utf-8">
<title>Vantix Imagery — Visual Interactive 3D Media for Real Estate</title>
<link rel="stylesheet" href="https://fonts.googleapis.com/css2?family=Raleway:wght@400;500;600;700;800&family=Open+Sans:wght@400;600;700&display=swap">
<style>
:root{
  --blue:#1f8fd7;
  --blue-bright:#32a6d6;
  --blue-deep:#0355a3;
  --blue-mid:#3176b5;
  --blue-soft:#85cae6;
  --blue-pale:#cee9f5;
  --grey-bg:#ebebeb;
  --grey-box:#e9e9e9;
  --ink:#2b2b2b;
  --ink-soft:#6a6a6a;
  --white:#ffffff;
  --night:#060a10;
  --footer:#000000;
}
*{box-sizing:border-box;margin:0;padding:0}
html,body{width:1200px;height:3529px;overflow:hidden}
body{position:relative;font-family:"Raleway",sans-serif;color:var(--ink);background:var(--white)}
.abs{position:absolute}
section,header,footer{position:absolute;left:0;width:1200px;overflow:hidden}

/* hero */
.hero{top:0;height:482px;background:var(--night)}
.hero-photo{position:absolute;inset:0;background:linear-gradient(180deg,#5b7590 0%,#3b5671 30%,#1e2f42 60%,#0a111b 100%)}
.nav{position:absolute;top:0;left:0;width:1200px;height:72px;background:rgba(5,12,22,.55)}
.brand{position:absolute;left:266px;top:20px;font-weight:700;font-size:24px;color:var(--white);letter-spacing:1px}
.nav-links{position:absolute;left:480px;top:27px;display:flex;gap:6px;list-style:none}
.nav-links li{font-family:"Open Sans",sans-serif;font-size:10px;font-weight:600;color:var(--white);padding:5px 10px}
.nav-links li.active{background:var(--blue-bright)}
.hero-rule{position:absolute;left:0;top:358px;width:1200px;height:5px;background:var(--blue-bright)}
.hero-band{position:absolute;left:0;top:363px;width:1200px;height:119px;background:rgba(4,10,18,.82)}
.hero-kicker{position:absolute;top:376px;width:100%;text-align:center;font-size:15px;font-weight:700;letter-spacing:4px;color:var(--white)}
.hero-title{position:absolute;top:388px;width:100%;text-align:center;font-size:58px;font-weight:500;letter-spacing:6px;color:var(--blue-bright);line-height:1}
.hero-sub{position:absolute;top:437px;width:100%;text-align:center;font-size:24px;font-weight:800;letter-spacing:3px;color:var(--white)}

/* process */
.process{top:482px;height:436px;background:var(--grey-bg)}
.process-head{position:absolute;top:60px;width:100%;text-align:center;font-size:28px}
.process-head .brand-name{font-weight:700;color:var(--blue-bright)}
.process-head .label{font-weight:400;color:#9a9a9a;font-size:24px;margin-left:6px}
.step{position:absolute;top:162px;width:240px;text-align:center}
.step .ring{width:124px;height:124px;border-radius:50%;background:var(--white);margin:0 auto;display:flex;align-items:center;justify-content:center;box-shadow:0 0 0 6px #dcdcdc}
.step h3{margin-top:26px;font-size:21px;font-weight:700;color:var(--ink)}
.step p{margin-top:8px;font-family:"Open Sans",sans-serif;font-size:16px;color:var(--ink-soft);line-height:1.35}
.step p b{color:var(--blue-bright);font-weight:600}
.step-link{position:absolute;top:222px;height:3px;background:var(--white)}
.step-time{position:absolute;top:244px;font-family:"Open Sans",sans-serif;font-size:18px;font-weight:700;color:var(--blue-bright)}

/* features */
.features{top:918px;height:710px;background:var(--blue)}
.features-photo{position:absolute;inset:0;background:linear-gradient(180deg,#2a97da 0%,#1f8fd7 50%,#1a86cf 100%)}
.features h2{position:absolute;top:38px;width:100%;text-align:center;font-size:34px;font-weight:600;letter-spacing:5px;color:var(--white)}
.feature-frame{position:absolute;left:141px;top:98px;width:918px;height:542px;background:var(--white);padding:14px}
.feature-list{width:100%;height:100%;background:var(--grey-box);list-style:none;padding-top:38px}
.feature-list li{display:flex;align-items:center;height:97px;padding-left:108px;font-size:24px;font-weight:500;letter-spacing:.6px;color:var(--ink)}
.feature-list svg{width:58px;height:58px;margin-right:40px}
.feature-list .num{width:46px}

/* portals */
.portals{top:1628px;height:431px;background:var(--grey-bg);text-align:center}
.portals .lead{position:absolute;top:60px;width:100%;font-size:24px;letter-spacing:1.5px;color:var(--ink);line-height:1.85}
.portals .lead b{color:var(--blue-bright);font-weight:600}
.portal{position:absolute;top:200px;display:flex;align-items:center;gap:12px;font-size:40px;font-weight:700;color:var(--ink)}
.portal .mark{width:44px;height:44px;border-radius:50%;background:#d7263d}
.portal-divider{position:absolute;left:638px;top:192px;width:2px;height:64px;background:#bcbcbc}
.portals .cta{position:absolute;top:307px;width:100%;font-size:26px;font-weight:700;letter-spacing:1px;color:var(--blue-bright)}
.portals .contact{position:absolute;top:350px;width:100%;font-family:"Open Sans",sans-serif;font-size:24px;letter-spacing:1.5px;color:var(--ink)}

/* advantages */
.advantages{top:2059px;height:689px;background:var(--blue)}
.advantages h2{position:absolute;top:60px;width:100%;text-align:center;font-size:34px;font-weight:700;color:var(--white)}
.advantages h2 .brand-name{font-size:40px;font-weight:800;margin:0 10px}
.perk{position:absolute;width:200px;text-align:center}
.perk .dot{width:124px;height:124px;border-radius:50%;background:var(--white);margin:0 auto;display:flex;align-items:center;justify-content:center}
.perk p{margin-top:14px;font-size:14px;font-weight:700;color:var(--white);line-height:1.35}
.perk-line{position:absolute;height:3px;background:var(--white)}
.advantages .ask{position:absolute;top:570px;width:100%;text-align:center;font-size:27px;letter-spacing:1.5px;color:var(--blue-pale)}
.advantages .reach{position:absolute;top:610px;width:100%;text-align:center;font-family:"Open Sans",sans-serif;font-size:26px;font-weight:700;letter-spacing:1px;color:var(--white)}

/* contact */
.contact-area{top:2748px;height:306px}
.map-fill{position:absolute;inset:0;background:linear-gradient(135deg,#e6ecd9 0%,#eef0e8 45%,#dfe7d2 100%)}
.contact-disc{position:absolute;left:196px;top:-40px;width:450px;height:450px;border-radius:50%;background:var(--blue-bright)}
.contact-area h2{position:absolute;left:270px;top:22px;font-size:28px;font-weight:700;color:var(--white)}
.contact-area .tag{position:absolute;left:270px;top:56px;font-size:12px;color:var(--blue-pale)}
.field{position:absolute;background:var(--white);height:24px;font-family:"Open Sans",sans-serif;font-size:9px;color:#8a8a8a;padding:6px 8px}
.submit{position:absolute;left:340px;top:268px;width:120px;height:26px;background:var(--white);color:var(--blue-bright);font-size:11px;font-weight:700;letter-spacing:1px;text-align:center;line-height:26px}
.map-pin{position:absolute;left:808px;top:112px}

/* customers */
.customers{top:3054px;height:158px;background:#f3f3f3}
.customers h2{position:absolute;top:22px;width:100%;text-align:center;font-size:24px;font-weight:700;color:var(--blue-bright)}
.badge-row{position:absolute;left:34px;top:60px;display:flex;gap:8px}
.badge{width:88px;height:66px;background:var(--white);border:1px solid #dcdcdc;display:flex;align-items:center;justify-content:center}
.badge span{display:block;width:60px;height:34px;border-radius:18px;background:var(--blue-soft)}
.badge:nth-child(3n+2) span{background:var(--blue-deep);border-radius:4px}
.badge:nth-child(3n) span{background:var(--blue-mid);border-radius:50%;width:40px;height:40px}

/* footer */
.site-footer{top:3212px;height:317px;background:var(--footer);color:#cfcfcf}
.col{position:absolute;top:50px;width:170px;font-family:"Open Sans",sans-serif;font-size:9px;line-height:1.6}
.col h4{font-family:"Raleway",sans-serif;font-size:14px;font-weight:700;color:var(--blue-bright);margin-bottom:14px}
.col p{margin-bottom:10px}
.col .meta{color:var(--blue-bright);font-size:8px;display:block}
.col .hl{color:var(--blue-bright)}
.signup{display:flex;margin-top:16px}
.signup span{flex:1;height:20px;background:#e9e9e9;color:#888;font-size:8px;padding:4px 6px}
.signup b{width:26px;height:20px;background:var(--blue-bright);color:var(--white);font-size:8px;text-align:center;line-height:20px}
.socials{display:flex;gap:10px;margin-top:18px}
.socials span{width:52px;height:52px;border-radius:50%;background:var(--blue-bright);color:var(--white);font-size:9px;font-weight:700;display:flex;align-items:center;justify-content:center}
.copyright{position:absolute;left:0;top:290px;width:1200px;padding:0 247px;font-family:"Open Sans",sans-serif;font-size:9px;color:var(--blue-soft)}
</style>
</head>
<body>

<header class="hero">
  <div class="hero-photo" role="img" aria-label="Upward view of glass office towers against a cloudy sky"></div>
  <nav class="nav">
    <div class="brand">Vantix Imagery</div>
    <ul class="nav-links">
      <li class="active">HOME</li><li>ABOUT US</li><li>PROCESS</li><li>COMPLEMENTARY FEATURES</li><li>OUR VISION</li><li>CONTACT</li>
    </ul>
  </nav>
  <div class="hero-rule"></div>
  <div class="hero-band"></div>
  <p class="hero-kicker">IMMERSIVE 3D AND VISUALLY RICH 2D MEDIA SOLUTIONS</p>
  <h1 class="hero-title">VISUAL INTERACTIVE</h1>
  <p class="hero-sub">3D MEDIA FOR REAL ESTATE</p>
</header>

<section class="process">
  <h2 class="process-head"><span class="brand-name">Vantix Imagery</span><span class="label">Process</span></h2>
  <div class="step-link" style="left:417px;width:132px"></div>
  <div class="step-link" style="left:683px;width:132px"></div>
  <div class="step-time" style="left:446px">2 hrs</div>
  <div class="step-time" style="left:713px">48 hrs</div>

  <div class="step" style="left:209px">
    <div class="ring">
      <svg width="62" height="62" viewBox="0 0 62 62" fill="none" stroke="var(--blue-bright)" stroke-width="3"><rect x="5" y="16" width="52" height="36" rx="5"/><path d="M20 16l4-7h14l4 7"/><circle cx="31" cy="34" r="10"/><circle cx="31" cy="34" r="4"/></svg>
    </div>
    <h3>Scan</h3>
    <p>Capture a space<br>in <b>3D</b></p>
  </div>
  <div class="step" style="left:485px">
    <div class="ring">
      <svg width="66" height="62" viewBox="0 0 66 62" fill="none" stroke="var(--blue-bright)" stroke-width="3"><path d="M18 46H14a10 10 0 0 1 0-20 16 16 0 0 1 31-6 12 12 0 0 1 7 26h-4"/><path d="M33 52V30M25 38l8-8 8 8"/></svg>
    </div>
    <h3>Upload</h3>
    <p>Process &amp; store<br>in the <b>cloud</b></p>
  </div>
  <div class="step" style="left:751px">
    <div class="ring">
      <svg width="40" height="66" viewBox="0 0 40 66" fill="none" stroke="var(--blue-bright)" stroke-width="3"><rect x="5" y="3" width="30" height="60" rx="5"/><path d="M5 12h30M5 52h30"/><circle cx="20" cy="57.5" r="1.5"/></svg>
    </div>
    <h3>View</h3>
    <p>Experience via<br><b>web &amp; mobile</b></p>
  </div>
</section>

<section class="features">
  <div class="features-photo" role="img" aria-label="Faint blue-tinted city towers behind the features panel"></div>
  <h2>COMPLEMENTARY FEATURES</h2>
  <div class="feature-frame">
    <ul class="feature-list">
      <li><svg viewBox="0 0 58 58" fill="none" stroke="var(--blue-mid)" stroke-width="2.5"><rect x="3" y="8" width="52" height="42" rx="2"/><path d="M3 17h52"/><circle cx="9" cy="12.5" r="1"/><circle cx="14" cy="12.5" r="1"/></svg><span class="num">1.</span>3D tour (integrated into all portals)</li>
      <li><svg viewBox="0 0 58 58" fill="none" stroke="var(--blue-mid)" stroke-width="2.5"><path d="M26 6h28v46H4V28h22z"/><path d="M26 28v12M4 40h14M40 28h14"/></svg><span class="num">2.</span>Traditional floor plan (with measurements)</li>
      <li><svg viewBox="0 0 58 58" fill="none" stroke="var(--blue-mid)" stroke-width="2.5"><rect x="14" y="4" width="36" height="44"/><path d="M8 10v44h36"/><path d="M20 14h24M20 21h24M20 28h24M20 35h24M20 42h16"/></svg><span class="num">3.</span>Company branding and digital presense</li>
      <li><svg viewBox="0 0 58 58" fill="none" stroke="var(--blue-mid)" stroke-width="2.5"><path d="M4 8h50M8 8v32h42V8M29 4v4M29 40v8M20 54l9-6 9 6"/><path d="M14 32l10-10 8 6 12-12"/></svg><span class="num">4.</span>Fortnightly analytic reports</li>
      <li><svg viewBox="0 0 58 58" fill="none" stroke="var(--blue-mid)" stroke-width="2.5"><rect x="3" y="6" width="48" height="40" rx="2"/><path d="M3 15h48"/><text x="11" y="35" font-size="11" font-family="Open Sans,sans-serif" fill="var(--blue-mid)" stroke="none" font-weight="700">www</text><circle cx="46" cy="45" r="9" fill="var(--blue-mid)" stroke="none"/><path d="M41.5 45l3 3 6-6" stroke="#fff"/></svg><span class="num">5.</span>Leading web integration and backend support</li>
    </ul>
  </div>
</section>

<section class="portals">
  <p class="lead">Stop buyers in their tracks with an engaging <b>3D Tour</b><br>Now available on</p>
  <div class="portal" style="left:282px"><span class="mark"></span>homelistly</div>
  <div class="portal-divider"></div>
  <div class="portal" style="left:682px">Parcelo</div>
  <p class="cta">Book your 3D Tour Today.</p>
  <p class="contact">info@vantiximagery.com.au &nbsp;|&nbsp; 1 800 555 019</p>
</section>

<section class="advantages">
  <h2>What sets <span class="brand-name">Vantix Imagery</span> apart from the rest</h2>

  <div class="perk-line" style="left:311px;top:233px;width:560px"></div>
  <div class="perk-line" style="left:311px;top:428px;width:560px"></div>

  <div class="perk" style="left:211px;top:174px">
    <div class="dot"><div role="img" aria-label="Outline of Australia" style="width:70px;height:56px;border-radius:40% 50% 45% 35%;background:var(--blue-bright)"></div></div>
    <p>Australia's leading<br>3D tour provider</p>
  </div>
  <div class="perk" style="left:399px;top:174px">
    <div class="dot"><svg width="66" height="56" viewBox="0 0 66 56" fill="none" stroke="var(--blue-bright)" stroke-width="3"><rect x="3" y="4" width="60" height="48" rx="3"/><path d="M3 15h60"/></svg></div>
    <p>Customized branded<br>web players</p>
  </div>
  <div class="perk" style="left:582px;top:174px">
    <div class="dot"><svg width="62" height="62" viewBox="0 0 58 58" fill="none" stroke="var(--blue-bright)" stroke-width="3"><path d="M26 6h28v46H4V28h22z"/><path d="M26 28v12M4 40h14"/></svg></div>
    <p>Fortnightly<br>analytics reviews</p>
  </div>
  <div class="perk" style="left:771px;top:174px">
    <div class="dot"><svg width="66" height="60" viewBox="0 0 58 54" fill="none" stroke="var(--blue-bright)" stroke-width="2.5"><rect x="3" y="4" width="46" height="38" rx="2"/><path d="M3 13h46"/><text x="10" y="32" font-size="11" font-family="Open Sans,sans-serif" fill="var(--blue-bright)" stroke="none" font-weight="700">www</text><circle cx="46" cy="42" r="9" fill="var(--blue-bright)" stroke="none"/><path d="M41.5 42l3 3 6-6" stroke="#fff"/></svg></div>
    <p>Leading web<br>integration &amp; backend</p>
  </div>

  <div class="perk" style="left:211px;top:369px">
    <div class="dot"><svg width="76" height="46" viewBox="0 0 76 46" fill="var(--blue-bright)"><path d="M6 6h64a4 4 0 0 1 4 4v20a4 4 0 0 1-4 4H50l-6-8h-12l-6 8H6a4 4 0 0 1-4-4V10a4 4 0 0 1 4-4z"/></svg></div>
    <p>VR optimisation</p>
  </div>
  <div class="perk" style="left:399px;top:369px">
    <div class="dot"><svg width="60" height="64" viewBox="0 0 60 64" fill="none" stroke="var(--blue-bright)" stroke-width="3"><path d="M30 44S14 28 14 19a16 16 0 0 1 32 0c0 9-16 25-16 25z"/><circle cx="30" cy="19" r="6"/><path d="M14 40L4 60h52L46 40"/></svg></div>
    <p>National Network</p>
  </div>
  <div class="perk" style="left:582px;top:369px">
    <div class="dot"><svg width="62" height="62" viewBox="0 0 62 62" fill="none" stroke="var(--blue-bright)" stroke-width="3"><path d="M52 20a24 24 0 1 0 2 16"/><path d="M54 8v12H42"/><text x="17" y="38" font-size="18" font-family="Open Sans,sans-serif" font-weight="700" fill="var(--blue-bright)" stroke="none">24</text></svg></div>
    <p>24hr turn around</p>
  </div>
  <div class="perk" style="left:771px;top:369px">
    <div class="dot"><svg width="56" height="62" viewBox="0 0 56 62" fill="none" stroke="var(--blue-bright)" stroke-width="3"><rect x="14" y="4" width="38" height="46"/><path d="M6 12v46h38"/><path d="M20 14h26M20 22h26M20 30h26M20 38h18"/></svg></div>
    <p>Branded material</p>
  </div>

  <p class="ask">If you have any questions please do not hesitate to contact:</p>
  <p class="reach">info@vantiximagery.com.au &nbsp;|&nbsp; 1 800 555 019</p>
</section>

<section class="contact-area">
  <div class="map-fill" role="img" aria-label="Street map of the suburbs around the office"></div>
  <div class="contact-disc"></div>
  <h2>CONTACT US</h2>
  <p class="tag">We Can Help You</p>
  <div class="field" style="left:263px;top:78px;width:130px">Name</div>
  <div class="field" style="left:405px;top:78px;width:131px">Email</div>
  <div class="field" style="left:263px;top:112px;width:273px">Phone Number</div>
  <div class="field" style="left:263px;top:146px;width:273px">Address</div>
  <div class="field" style="left:263px;top:180px;width:273px;height:66px">Message</div>
  <div class="submit">SUBMIT</div>
  <svg class="map-pin" width="50" height="70" viewBox="0 0 50 70"><path d="M25 68S4 40 4 24a21 21 0 0 1 42 0c0 16-21 44-21 44z" fill="var(--blue-bright)"/><circle cx="25" cy="24" r="9" fill="#fff"/></svg>
</section>

<section class="customers">
  <h2>OUR CUSTOMERS</h2>
  <div class="badge-row">
    <div class="badge"><span></span></div><div class="badge"><span></span></div><div class="badge"><span></span></div>
    <div class="badge"><span></span></div><div class="badge"><span></span></div><div class="badge"><span></span></div>
    <div class="badge"><span></span></div><div class="badge"><span></span></div><div class="badge"><span></span></div>
    <div class="badge"><span></span></div><div class="badge"><span></span></div><div class="badge"><span></span></div>
  </div>
</section>

<footer class="site-footer">
  <div class="col" style="left:247px">
    <h4>Newsletter Signup</h4>
    <p>Get new tours, tips for selling and studio news sent to your inbox once a month.</p>
    <div class="signup"><span>Email Address</span><b>Go</b></div>
    <div class="socials"><span>Zembol</span><span>Quillnest</span><span>Gleamory</span></div>
  </div>
  <div class="col" style="left:440px">
    <h4>Vantix Imagery</h4>
    <p>Vantix Imagery creates engaging and immersive online viewing experiences through the latest 3D camera technology and virtual reality.</p>
    <p>Through scanning and modelling, our team captures your property in great detail and turns it into rich, meaningful marketing that buyers can explore from any screen.</p>
  </div>
  <div class="col" style="left:638px">
    <h4>Recent Tweets</h4>
    <p>New dollhouse views are now live for our latest listings.<span class="meta">2 hours ago</span></p>
    <p>Walk through any home in 3D from your phone today.<span class="meta">5 hours ago</span></p>
    <p>Our scanning team is now booking across the state.<span class="meta">1 day ago</span></p>
  </div>
  <div class="col" style="left:824px">
    <h4>Contact Us</h4>
    <p>Brightframe Pty Ltd, 12 Alder Rd, Eastvale VIC 3999<br>Office Hours: 9am – 5pm, Mon – Fri</p>
    <p><span class="hl">Ph:</span> 1 800 555 019<br><span class="hl">Fax:</span> 1 800 555 020<br><span class="hl">Email:</span> info@vantiximagery.com.au</p>
  </div>
  <p class="copyright">Copyright 2017 Vantix Imagery. All Rights Reserved.</p>
</footer>

</body>
</html>
```